Layout for site fence advertising - length approx. 250 cm x 125 cm

The advertising will later be printed on a PVC film and used for events or on sports fields.

Main services :
Your regional contact at
Real estate and business financing
independent insurance advice

```html
<!DOCTYPE html>
<html lang="en">
<head>
<meta charset="utf-8">
<title>Lindhof Vermögensberatung – Fence Banner</title>
<link rel="stylesheet" href="https://fonts.googleapis.com/css2?family=Montserrat:wght@400;500;600;700;800&display=swap">
<style>
  :root {
    --page-bg: #8f8f8f;
    --navy-deep: #0a2c6e;
    --navy-mid: #0f3f98;
    --blue-bright: #1a5ccc;
    --white: #ffffff;
    --accent-blue: #1f50c2;
    --text-grey: #4a4a4a;
    --photo-dark: #1d2233;
    --photo-skin: #c98a6c;
  }
  * { box-sizing: border-box; margin: 0; padding: 0; }
  html, body { width: 972px; height: 1200px; overflow: hidden; }
  body {
    background: linear-gradient(135deg, #7a7a7a, #a9a9a9);
    font-family: "Montserrat", sans-serif;
    position: relative;
  }
  .banner {
    position: absolute;
    left: 20px; top: 367px;
    width: 932px; height: 466px;
    background: linear-gradient(100deg, var(--navy-deep) 0%, var(--navy-mid) 55%, var(--blue-bright) 100%);
    overflow: hidden;
    box-shadow: -4px 6px 10px rgba(0,0,0,0.35);
    color: var(--white);
  }
  .decor-circle {
    position: absolute;
    left: 430px; top: 35px;
    width: 260px; height: 260px;
    border-radius: 50%;
    border: 16px solid rgba(10,40,110,0.35);
  }
  .brand-ring {
    position: absolute;
    left: 45px; top: 38px;
    width: 130px; height: 130px;
    border-radius: 50%;
    border: 4px solid var(--white);
  }
  .brand-divider {
    position: absolute;
    left: 189px; top: 37px;
    width: 3px; height: 133px;
    background: var(--white);
  }
  .brand-name {
    position: absolute;
    left: 200px; top: 74px;
    font-weight: 600;
    font-size: 25px;
    letter-spacing: -0.2px;
    white-space: nowrap;
  }
  .brand-name small { font-size: 18px; }
  .brand-tagline {
    position: absolute;
    left: 200px; top: 106px;
    font-weight: 600;
    font-size: 17px;
    white-space: nowrap;
  }
  .services {
    position: absolute;
    left: 43px; top: 218px;
    list-style: none;
  }
  .services-heading {
    font-weight: 700;
    font-size: 32px;
    margin-bottom: 10px;
    white-space: nowrap;
  }
  .service {
    display: flex; align-items: center;
    font-weight: 500;
    font-size: 33px;
    line-height: 44px;
    white-space: nowrap;
  }
  .service svg { width: 26px; height: 26px; margin-right: 14px; flex: none; }
  .contact-band {
    position: absolute;
    left: 0; top: 393px;
    width: 932px; height: 73px;
    background: var(--white);
    display: flex; align-items: center;
    padding-left: 43px;
  }
  .contact-icon { width: 22px; height: 22px; flex: none; }
  .phone {
    margin-left: 12px;
    font-weight: 800;
    font-size: 32px;
    color: var(--accent-blue);
  }
  .sep {
    width: 2px; height: 28px; background: var(--text-grey);
    margin: 0 10px;
  }
  .web {
    margin-left: 10px;
    font-size: 23px;
    color: var(--text-grey);
  }
  .web b { color: var(--accent-blue); font-weight: 700; }
  .portrait {
    position: absolute;
    left: 620px; top: 40px;
    width: 312px; height: 426px;
    background:
      radial-gradient(ellipse 38% 30% at 52% 32%, var(--photo-skin) 0%, rgba(201,138,108,0.5) 55%, rgba(201,138,108,0) 100%),
      linear-gradient(180deg, rgba(29,34,51,0) 0%, rgba(29,34,51,0) 50%, var(--photo-dark) 72%, var(--photo-dark) 100%);
    clip-path: polygon(30% 0, 80% 0, 88% 40%, 100% 58%, 100% 100%, 0 100%, 8% 85%, 18% 70%, 22% 40%);
  }
</style>
</head>
<body>
  <section class="banner">
    <div class="decor-circle"></div>

    <div class="brand-ring"></div>
    <div class="brand-divider"></div>
    <p class="brand-name">Lindhof Vermögensberatung <small>GmbH</small></p>
    <p class="brand-tagline">Finanzieren, Versichern, Vorsorgen</p>

    <ul class="services">
      <li class="services-heading">Your regional contact at</li>
      <li class="service">
        <svg viewBox="0 0 26 26" fill="none" stroke="#fff" stroke-width="2.4"><rect x="2" y="4" width="20" height="20"/><path d="M7 13l5 5 12-14"/></svg>
        Real estate and business financing
      </li>
      <li class="service">
        <svg viewBox="0 0 26 26" fill="none" stroke="#fff" stroke-width="2.4"><rect x="2" y="4" width="20" height="20"/><path d="M7 13l5 5 12-14"/></svg>
        Independent insurance advice
      </li>
    </ul>

    <div class="contact-band">
      <svg class="contact-icon" viewBox="0 0 24 24"><circle cx="12" cy="12" r="11" fill="#1f50c2"/><path d="M8 6.5c-1 1-1 3 1 6s4.5 5 6 5l1.5-1.5-2.3-2-1.2.9c-1-.5-2.4-2-2.9-3l.9-1.2-2-2.3z" fill="#fff"/></svg>
      <span class="phone">4821 903 517</span>
      <span class="sep"></span>
      <svg class="contact-icon" viewBox="0 0 24 24" fill="none" stroke="#1f50c2" stroke-width="1.6"><circle cx="12" cy="12" r="10" fill="#1f50c2"/><circle cx="12" cy="12" r="6.5" stroke="#fff"/><ellipse cx="12" cy="12" rx="2.8" ry="6.5" stroke="#fff"/><path d="M5.5 12h13M6.5 9h11M6.5 15h11" stroke="#fff"/></svg>
      <span class="web">www.<b>lindhof-finanz</b>.com</span>
    </div>

    <div class="portrait" role="img" aria-label="Portrait photo of the consultant in a dark suit and white shirt"></div>
  </section>
</body>
</html>
```